Business Card Design

I need a card design for Melbourne based business in Australia, called M P Concrete Services. We Concrete and excavate. Concreteing is main part of business.Commercial ,Residential and industrial.We want to be known as M P C (services) as form of abbreviation.We would like to highlight the initials with contact phone. A clean straight edge design. We have no color preference and would prefer a design that can easily be used on all parts of our business including clothing,vechiles and stationary

Industry/Entity Type

Business

Contact Information for Business Card

Hugh 0491 570 156
Peter 0491 570 157
mpcsercices@quollmail.com

```html
<!DOCTYPE html>
<html lang="en">
<head>
<meta charset="utf-8">
<title>M P Concrete Services – Business Card</title>
<link href="https://fonts.googleapis.com/css2?family=Exo+2:wght@400&display=swap" rel="stylesheet">
<style>
  :root {
    --backdrop: #e4e4e4;
    --card: #f7f7f7;
    --card-shade: #ececec;
    --bar: #8c8c8c;
    --ink: #2a2a2a;
    --ink-soft: #3a3a3a;
    --rule: #555555;
    --icon: #2a2a2a;
  }
  * { margin: 0; padding: 0; box-sizing: border-box; }
  html, body {
    width: 1200px;
    height: 871px;
    overflow: hidden;
    background: var(--backdrop);
  }
  .card {
    position: absolute;
    left: 150px;
    top: 160px;
    width: 900px;
    height: 550px;
    background: radial-gradient(ellipse at 55% 40%, #ffffff 0%, var(--card) 45%, var(--card-shade) 100%);
    box-shadow: 0 6px 24px rgba(0, 0, 0, 0.18);
    font-family: "Exo 2", sans-serif;
    font-weight: 400;
  }
  .card__bar {
    position: absolute;
    left: 0;
    top: 0;
    width: 325px;
    height: 42px;
    background: var(--bar);
  }
  .card__name {
    position: absolute;
    left: 0;
    top: 229px;
    width: 412px;
    text-align: center;
    font-weight: 400;
    font-size: 27px;
    line-height: 40px;
    color: var(--ink);
    white-space: nowrap;
  }
  .card__divider {
    position: absolute;
    left: 412px;
    top: 140px;
    width: 2px;
    height: 215px;
    background: var(--rule);
  }
  .contacts {
    position: absolute;
    left: 440px;
    top: 150px;
    list-style: none;
    font-size: 27px;
    color: var(--ink-soft);
  }
  .contacts__row {
    display: flex;
    align-items: center;
    height: 40px;
    white-space: nowrap;
  }
  .contacts__icon {
    width: 26px;
    height: 26px;
    margin-right: 14px;
    flex: none;
  }
  .contacts__row--indent { padding-left: 40px; }
  .contacts__person { display: inline-block; width: 78px; }
</style>
</head>
<body>
  <section class="card" aria-label="M P Concrete Services business card">
    <div class="card__bar"></div>
    <h1 class="card__name">M P Concrete Services</h1>
    <div class="card__divider"></div>
    <ul class="contacts">
      <li class="contacts__row">
        <svg class="contacts__icon" viewBox="0 0 26 26" aria-hidden="true">
          <circle cx="13" cy="13" r="13" fill="var(--icon)"/>
          <path d="M8.6 6.5l2.6 0.2 1.1 3.3-1.7 1.3c0.8 1.8 2.2 3.2 4 4l1.3-1.7 3.3 1.1 0.2 2.6c-0.6 1-1.8 1.6-3 1.4-4.7-0.9-8.4-4.6-9.2-9.2-0.2-1.2 0.4-2.4 1.4-3z" fill="#ffffff"/>
        </svg>
        <span class="contacts__person">Hugh</span><span>0491 570 156</span>
      </li>
      <li class="contacts__row contacts__row--indent">
        <span class="contacts__person">Peter</span><span>0491 570 157</span>
      </li>
      <li class="contacts__row">
        <svg class="contacts__icon" viewBox="0 0 26 26" aria-hidden="true">
          <circle cx="13" cy="13" r="13" fill="var(--icon)"/>
          <rect x="6.5" y="8.5" width="13" height="9" fill="none" stroke="#ffffff" stroke-width="1.6"/>
          <path d="M6.5 8.5l6.5 5 6.5-5" fill="none" stroke="#ffffff" stroke-width="1.6"/>
        </svg>
        <span>mpcsercices@quollmail.com</span>
      </li>
    </ul>
  </section>
</body>
</html>
```